Industrial & commercial facility maintenance flyer

Design a 2 sided flyer that outlines our core business unit services. One side shall be for our industrial maintenance division while the other will be focused on our commercial maintenance division.

Media from website here: https://files.velnorashare.com/folders/7K3QzP91mXwRtLaBvYcNe4HdUsFj

Target Market(s)

Industrial and commercial facility maintenance companies and professionals

Industry/Entity Type

Maintenance

Font styles to use
Serif

Colors
ffffff
2f73b4
0455a3
cfdfed

Requirements
Must have
• Several photos of each applicable service. Reference existing website (www.tkrvb.com). Use of the blue and grey scheme of our current logo.
Nice to have
• Our logo design across the top with our contact information on the bottom.

```html
<!DOCTYPE html>
<html lang="en">
<head>
<meta charset="utf-8">
<title>Keystone Upkeep Solutions – Two-Sided Flyer</title>
<link href="https://fonts.googleapis.com/css2?family=Montserrat:wght@300;400;600;700&display=swap" rel="stylesheet">
<style>
  :root {
    --brand-blue: #0455a3;
    --brand-blue-light: #2f73b4;
    --brand-ice: #cfdfed;
    --paper: #ffffff;
    --panel-grey: #e5e5e5;
    --ink: #3a3a3a;
    --ink-soft: #555b61;
    --stage: #eeeeee;
  }
  * { box-sizing: border-box; margin: 0; padding: 0; }
  html, body { width: 1200px; height: 845px; overflow: hidden; background: var(--stage); }
  body { position: relative; font-family: "Montserrat", sans-serif; color: var(--ink); }

  .flyer { position: absolute; top: 30px; width: 553px; height: 774px; background: var(--paper); overflow: hidden; }
  .flyer--industrial { left: 30px; }
  .flyer--management { left: 614px; }

  .brand { position: absolute; top: 0; left: 0; width: 100%; height: 122px; }
  .brand__mark { position: absolute; left: 92px; top: 26px; width: 72px; height: 72px; border-radius: 50%; background: #4b4f54; }
  .brand__name { position: absolute; left: 180px; top: 36px; font-size: 22px; font-weight: 600; color: var(--brand-blue); letter-spacing: 0.2px; white-space: nowrap; }
  .brand__rule { position: absolute; left: 182px; top: 70px; width: 312px; height: 1px; background: #4b4f54; }
  .brand__divisions { position: absolute; left: 182px; top: 78px; font-size: 11.5px; font-weight: 600; letter-spacing: 3.6px; color: #4b4f54; white-space: nowrap; }

  .hero { position: absolute; top: 122px; left: 0; width: 100%; height: 145px; }
  .hero--city { background: linear-gradient(90deg, #1e3f6e 0%, #3d5d82 35%, #6f8298 70%, #8d8a76 100%); }
  .hero--tower { background: linear-gradient(180deg, #c9d6e4 0%, #9fb1c6 45%, #4d5b6e 100%); }
  .hero__title { position: absolute; left: 0; width: 100%; text-align: center; color: var(--paper); font-weight: 700; text-shadow: 0 2px 4px rgba(0,0,0,0.35); }
  .hero--city .hero__title { top: 48px; font-size: 35px; }
  .hero--tower .hero__title { top: 36px; font-size: 34px; line-height: 36px; }

  .photo { position: absolute; }
  .photo--technician { left: 277px; top: 282px; width: 253px; height: 196px; background: linear-gradient(135deg, #e9e9e4 0%, #c9ccd0 45%, #2f5fb0 70%, #d9d6cc 100%); }
  .photo--plant { left: 24px; top: 501px; width: 252px; height: 198px; background: linear-gradient(160deg, #9aa8b2 0%, #6b7d86 40%, #c9a23a 65%, #50606a 100%); }

  .band { position: absolute; left: 0; width: 100%; }
  .band--grey { background: var(--panel-grey); }

  .section-title { position: absolute; font-size: 20.5px; font-weight: 400; line-height: 23px; color: var(--ink); }
  .copy { position: absolute; font-size: 12.8px; font-weight: 400; line-height: 15.2px; color: var(--ink-soft); }
  .copy--dense { font-size: 11.4px; line-height: 12.7px; }
  .copy--dense p + p { margin-top: 12px; }

  .benefits { position: absolute; left: 24px; top: 383px; list-style: none; font-size: 11.6px; font-weight: 600; line-height: 14px; color: var(--ink); }
  .benefits li { position: relative; padding-left: 16px; }
  .benefits li::before { content: ""; position: absolute; left: 2px; top: 5px; width: 4px; height: 4px; border-radius: 50%; background: var(--ink-soft); }

  .footer { position: absolute; left: 0; width: 100%; bottom: 0; background: var(--brand-blue); }
  .footer__box { position: absolute; left: 22px; width: 508px; border: 1px solid var(--paper); color: var(--paper); font-size: 18px; display: flex; align-items: center; justify-content: center; }
</style>
</head>
<body>

<!-- Side A: facility maintenance -->
<section class="flyer flyer--industrial">
  <header class="brand">
    <span class="brand__mark"></span>
    <span class="brand__name">Keystone Upkeep Solutions</span>
    <span class="brand__rule"></span>
    <span class="brand__divisions">INDUSTRIAL - COMMERCIAL - RETAIL</span>
  </header>

  <div class="hero hero--city" role="img" aria-label="Technician holding a wrench in front of a city skyline">
    <h1 class="hero__title">Facility Maintenance</h1>
  </div>

  <h2 class="section-title" style="left:22px; top:284px;">Retail Maintenance<br>Solutions</h2>
  <p class="copy" style="left:24px; top:338px; width:250px;">Keystone Upkeep Solutions knows how important it is to convert window shoppers to paying customers. We ensure that your business is always looking its best with our cost-effective maintenance programs. Our crew is available 24/7 to take care of any equipment or facility malfunction as quickly as possible.</p>
  <div class="photo photo--technician" role="img" aria-label="Maintenance technician in blue overalls carrying a toolbox beside a van"></div>

  <div class="band band--grey" style="top:493px; height:212px;"></div>
  <div class="photo photo--plant" role="img" aria-label="Interior of an industrial plant with heavy machinery"></div>
  <h2 class="section-title" style="left:288px; top:497px;">Retail Maintenance<br>Solutions</h2>
  <p class="copy" style="left:290px; top:551px; width:250px;">Keystone Upkeep Solutions knows how important it is to convert window shoppers to paying customers. We ensure that your business is always looking its best with our cost-effective maintenance programs. Our crew is available 24/7 to take care of any equipment or facility malfunction as quickly as possible.</p>

  <footer class="footer" style="height:69px;">
    <div class="footer__box" style="top:7px; height:43px;">adress area</div>
  </footer>
</section>

<!-- Side B: facility management -->
<section class="flyer flyer--management">
  <header class="brand">
    <span class="brand__mark"></span>
    <span class="brand__name">Keystone Upkeep Solutions</span>
    <span class="brand__rule"></span>
    <span class="brand__divisions">INDUSTRIAL - COMMERCIAL - RETAIL</span>
  </header>

  <div class="hero hero--tower" role="img" aria-label="Upward view of glass office towers against the sky">
    <h1 class="hero__title">Facility Management<br>Solutions</h1>
  </div>

  <h2 class="section-title" style="left:22px; top:280px; font-size:19.5px;">Facility Management Solutions</h2>
  <p class="copy copy--dense" style="left:24px; top:310px; width:520px;">Facility management is vital for any business to run smoothly. Consistently managing your facilities ensures that your building &amp; equipment is functioning properly, your systems are up to code, and worn parts are replaced. For your convenience, Keystone Upkeep Solution's facility management services can be integrated with our industrial or commercial maintenance services.</p>
  <ul class="benefits">
    <li>Integrated, single-source solution for all trades</li>
    <li>Powerful Computerized Maintenance Management System (CMMS)</li>
    <li>Streamline operations</li>
    <li>Improve bottom line</li>
  </ul>

  <div class="band band--grey" style="top:452px; height:220px;"></div>
  <h2 class="section-title" style="left:22px; top:460px; font-size:19.5px;">Facility Management Services You Can Rely On</h2>
  <div class="copy copy--dense" style="left:22px; top:493px; width:520px;">
    <p>As a single-source maintenance solution, we become an integrated component of your business's operation. Familiarity allows our teams and partners to perform repairs more quickly. With our cost effective maintenance programs, we can mitigate critical equipment failures saving you downtime.</p>
    <p>By integrating facility management with our other services, Keystone Upkeep provides a clear line of communication that is more effective, allowing problems to be addressed more quickly. We know the condition of your equipment, the layout of your facility, your company's long- and short-term goals, and problems that have occurred in the past. With all of that information and access, you can rest assured that we've got you covered.</p>
    <p>Let us provide you an integrated maintenance solution and rest easy knowing your facility is being cared for by the best in the industry!</p>
  </div>

  <footer class="footer" style="height:102px;">
    <div class="footer__box" style="top:10px; height:70px;">adress area</div>
  </footer>
</section>

</body>
</html>
```